Would like to reproduce this screen to look more modern

My app is a place for farmers to post jobs a when needing help around the Farm, and local farmhands can apply for the job. The Farmer can then review multiple applicants and select the one best fit for the task at hand. I'm trying to give my screens an updated look while keeping my current color scheme and flow. I would like for you guys to recreate this screen with an updated look the best you can. The main screen with the PX will stay the same. I put that in there to show our logo and our main colors. They look outdated. the other 2 screens are looking at the customers profile, and the screen that u fill out to post a new job.

Target Market(s)

Farmers and farm employees inside the US

Industry/Entity Type

Agriculture

Requirements
Must have
• the same components for the flow but a new look
Nice to have
• ...
Should not have
• Should not change any features, but we can change how buttons look

```html
<!DOCTYPE html>
<html lang="en">
<head>
<meta charset="utf-8">
<title>Fieldcrew – Create Job &amp; Profile</title>
<link href="https://fonts.googleapis.com/css2?family=Roboto:wght@400;500;700&display=swap" rel="stylesheet">
<style>
  :root {
    --bg: #e1eef8;
    --green: #44743b;
    --dark: #333333;
    --ink: #1f1f1f;
    --muted: #a8a8a8;
    --field: #ffffff;
    --surface: #f7f7f7;
  }
  * { box-sizing: border-box; margin: 0; padding: 0; }
  html, body { width: 1200px; height: 1200px; overflow: hidden; }
  body {
    background: var(--bg);
    font-family: "Roboto", sans-serif;
    color: var(--ink);
    position: relative;
  }
  .screen {
    position: absolute;
    border-radius: 56px;
    overflow: hidden;
    box-shadow: 0 18px 40px rgba(60, 90, 110, 0.18);
  }
  .screen > * { position: absolute; }
  .status-time { font-size: 18px; color: #1a1a1a; }
  .status-icons { display: flex; gap: 5px; align-items: center; }
  .appbar { left: 0; right: 0; top: 0; background: var(--green); }
  .appbar-title {
    left: 0; right: 0; text-align: center;
    color: #fff; font-weight: 500; font-size: 24px;
    transform: translateY(-50%);
  }

  /* Create job screen */
  .create { left: 107px; top: 86px; width: 474px; height: 1027px; background: #fff; }
  .create .appbar { height: 120px; box-shadow: 0 3px 6px rgba(0,0,0,0.12); }
  .section-title {
    left: 0; right: 0; top: 167px; text-align: center;
    font-size: 20px; font-weight: 500; transform: translateY(-50%);
  }
  .field-label { left: 41px; font-size: 17px; transform: translateY(-50%); }
  .field {
    left: 41px; width: 388px; height: 52px;
    background: var(--field); border-radius: 4px;
    box-shadow: 0 2px 8px rgba(0,0,0,0.07);
    display: flex; align-items: center; justify-content: space-between;
    padding: 0 28px 0 23px;
    font-size: 18px; color: var(--muted);
  }
  .caret { width: 0; height: 0; border-left: 8px solid transparent; border-right: 8px solid transparent; border-top: 9px solid #111; }
  .rate-option { top: 453px; display: flex; align-items: center; gap: 10px; font-size: 15px; line-height: 18px; color: var(--ink); }
  .radio { width: 26px; height: 26px; border-radius: 50%; border: 1.5px solid #555; display: flex; align-items: center; justify-content: center; }
  .radio.is-on::after { content: ""; width: 20px; height: 20px; border-radius: 50%; background: #111; }
  .create-button {
    left: 0; right: 0; bottom: 0; height: 84px; background: var(--dark);
    color: #fff; font-size: 26px; font-weight: 500; letter-spacing: 1.5px;
    display: flex; align-items: center; justify-content: center; padding-bottom: 2px;
  }

  /* Profile screen */
  .profile { left: 668px; top: 155px; width: 432px; height: 936px; background: var(--surface); }
  .profile .appbar { height: 109px; box-shadow: 0 3px 6px rgba(0,0,0,0.12); }
  .profile .appbar-title { font-size: 19px; font-weight: 700; }
  .profile-card { left: 25px; top: 141px; width: 382px; height: 141px; background: #fff; border-radius: 6px; }
  .avatar {
    left: 42px; top: 164px; width: 97px; height: 97px; border-radius: 8px;
    background: #f2f2f2; box-shadow: 0 4px 8px rgba(0,0,0,0.12);
    display: flex; align-items: center; justify-content: center;
  }
  .profile-name { left: 167px; top: 187px; font-size: 18px; font-weight: 500; transform: translateY(-50%); }
  .profile-id { left: 167px; top: 209px; font-size: 12px; transform: translateY(-50%); }
  .profile-rating { left: 167px; top: 228px; }
  .list-row {
    left: 25px; width: 381px; height: 65px; background: #fff;
    display: flex; align-items: center; padding-left: 16px; font-size: 16px; font-weight: 500;
  }
  .row-action { margin-left: auto; display: flex; align-items: center; gap: 8px; color: var(--muted); font-weight: 400; font-size: 16px; }
  .row-action svg { display: block; }
  .jobs-band {
    left: 0; right: 0; top: 597px; height: 49px; background: var(--green);
    color: #fff; font-size: 17px; font-weight: 700; display: flex; align-items: center; padding-left: 27px;
  }
  .count {
    width: 18px; height: 18px; border-radius: 50%; background: #1a1a1a; color: #fff;
    font-size: 11px; font-weight: 700; display: flex; align-items: center; justify-content: center; margin-right: 18px;
  }
</style>
</head>
<body>

<section class="screen create">
  <header class="appbar" style="height:120px"></header>
  <span class="status-time" style="left:28px;top:14px">9:41</span>
  <div class="status-icons" style="left:363px;top:18px">
    <svg width="22" height="14" viewBox="0 0 22 14"><rect x="0" y="9" width="4" height="5" fill="#111"/><rect x="6" y="6" width="4" height="8" fill="#111"/><rect x="12" y="3" width="4" height="11" fill="#111"/><rect x="18" y="0" width="4" height="14" fill="#111"/></svg>
    <svg width="20" height="14" viewBox="0 0 20 14"><path d="M10 13 L13 9.5 A5 5 0 0 0 7 9.5 Z M3.5 6.5 A9 9 0 0 1 16.5 6.5 L15 8 A7 7 0 0 0 5 8 Z M0.5 3.5 A13.5 13.5 0 0 1 19.5 3.5 L18 5 A11.5 11.5 0 0 0 2 5 Z" fill="#111"/></svg>
    <svg width="30" height="14" viewBox="0 0 30 14"><rect x="0.5" y="0.5" width="26" height="13" rx="3" fill="none" stroke="#111" opacity=".5"/><rect x="2" y="2" width="23" height="10" rx="2" fill="#111"/><rect x="28" y="4.5" width="2" height="5" rx="1" fill="#111" opacity=".5"/></svg>
  </div>
  <svg style="left:29px;top:74px" width="24" height="24" viewBox="0 0 24 24"><path d="M21 12H4M11 4l-8 8 8 8" fill="none" stroke="#fff" stroke-width="2.4" stroke-linecap="round" stroke-linejoin="round"/></svg>
  <h1 class="appbar-title" style="top:86px">FIELDCREW</h1>

  <h2 class="section-title">CREATE NEW JOB</h2>

  <label class="field-label" style="top:222px">Job Category</label>
  <div class="field" style="top:244px">Select Category<span class="caret"></span></div>

  <label class="field-label" style="top:333px">Job Title</label>
  <div class="field" style="top:355px">Enter the Title</div>

  <div class="rate-option" style="left:40px"><span class="radio is-on"></span><span>HOURLY<br>RATE ($)</span></div>
  <div class="rate-option" style="left:174px"><span class="radio"></span><span>FIXED<br>SALARY ($)</span></div>
  <div class="rate-option" style="left:325px"><span class="radio"></span><span>PER<br>ACRE ($)</span></div>

  <div class="field" style="top:514px;width:184px">From</div>
  <div class="field" style="top:514px;left:245px;width:184px">To</div>

  <label class="field-label" style="top:614px">Job Type</label>
  <div class="field" style="top:634px">Select Job Type<span class="caret"></span></div>

  <label class="field-label" style="top:723px">Equipment Provided</label>
  <div class="field" style="top:745px">Select Equipments<span class="caret"></span></div>

  <label class="field-label" style="top:834px;left:46px">Start Time and Date</label>
  <div class="field" style="top:856px">Select Start Date and Time<span class="caret"></span></div>

  <div class="create-button">CREATE JOB</div>
</section>

<section class="screen profile">
  <header class="appbar"></header>
  <span class="status-time" style="left:25px;top:13px">9:41</span>
  <div class="status-icons" style="left:329px;top:17px">
    <svg width="20" height="13" viewBox="0 0 22 14"><rect x="0" y="9" width="4" height="5" fill="#111"/><rect x="6" y="6" width="4" height="8" fill="#111"/><rect x="12" y="3" width="4" height="11" fill="#111"/><rect x="18" y="0" width="4" height="14" fill="#111"/></svg>
    <svg width="18" height="13" viewBox="0 0 20 14"><path d="M10 13 L13 9.5 A5 5 0 0 0 7 9.5 Z M3.5 6.5 A9 9 0 0 1 16.5 6.5 L15 8 A7 7 0 0 0 5 8 Z M0.5 3.5 A13.5 13.5 0 0 1 19.5 3.5 L18 5 A11.5 11.5 0 0 0 2 5 Z" fill="#111"/></svg>
    <svg width="28" height="13" viewBox="0 0 30 14"><rect x="0.5" y="0.5" width="26" height="13" rx="3" fill="none" stroke="#111" opacity=".5"/><rect x="2" y="2" width="23" height="10" rx="2" fill="#111"/><rect x="28" y="4.5" width="2" height="5" rx="1" fill="#111" opacity=".5"/></svg>
  </div>
  <svg style="left:27px;top:69px" width="24" height="20" viewBox="0 0 24 20"><path d="M0 2h24M0 10h24M0 18h24" stroke="#fff" stroke-width="2.4"/></svg>
  <h1 class="appbar-title" style="top:79px">MY PROFILE</h1>

  <div class="profile-card"></div>
  <div class="avatar">
    <svg width="58" height="68" viewBox="0 0 58 68"><circle cx="29" cy="16" r="16" fill="#000"/><path d="M0 60 C0 44 10 34 20 34 H38 C48 34 58 44 58 60 V62 A6 6 0 0 1 52 68 H6 A6 6 0 0 1 0 62 Z" fill="#000"/></svg>
  </div>
  <p class="profile-name">Daniel Hartwell</p>
  <p class="profile-id">48213097765</p>
  <svg class="profile-rating" width="25" height="24" viewBox="0 0 24 23"><path d="M12 1.5l3.1 6.6 7.2.9-5.3 5 1.4 7.1L12 17.6l-6.4 3.5L7 14 1.7 9l7.2-.9z" fill="none" stroke="#111" stroke-width="1.5" stroke-linejoin="round"/></svg>

  <div class="list-row" style="top:297px">User Details<span class="row-action">Edit Details<svg width="8" height="12" viewBox="0 0 8 12"><path d="M1.5 1l5 5-5 5" fill="none" stroke="#999" stroke-width="1.5"/></svg><i style="width:4px"></i></span></div>
  <div class="list-row" style="top:366px">Education Details<span class="row-action">Edit Details<svg width="8" height="12" viewBox="0 0 8 12"><path d="M1.5 1l5 5-5 5" fill="none" stroke="#999" stroke-width="1.5"/></svg><i style="width:4px"></i></span></div>
  <div class="list-row" style="top:435px">Farm Details<span class="row-action">Edit Details<svg width="8" height="12" viewBox="0 0 8 12"><path d="M1.5 1l5 5-5 5" fill="none" stroke="#999" stroke-width="1.5"/></svg><i style="width:4px"></i></span></div>
  <div class="list-row" style="top:503px">Farm Images<span class="row-action">Edit Details<svg width="8" height="12" viewBox="0 0 8 12"><path d="M1.5 1l5 5-5 5" fill="none" stroke="#999" stroke-width="1.5"/></svg><i style="width:4px"></i></span></div>

  <div class="jobs-band">FIELDCREW JOBS</div>

  <div class="list-row" style="top:659px;padding-left:20px">Applied Jobs<span class="row-action"><span class="count">2</span>View Details<svg width="8" height="12" viewBox="0 0 8 12"><path d="M1.5 1l5 5-5 5" fill="none" stroke="#999" stroke-width="1.5"/></svg></span></div>
  <div class="list-row" style="top:727px">Scheduled Jobs<span class="row-action"><span class="count">0</span>View Details<svg width="8" height="12" viewBox="0 0 8 12"><path d="M1.5 1l5 5-5 5" fill="none" stroke="#999" stroke-width="1.5"/></svg></span></div>
  <div class="list-row" style="top:795px">Recieved Jobs<span class="row-action"><span class="count">2</span>View Details<svg width="8" height="12" viewBox="0 0 8 12"><path d="M1.5 1l5 5-5 5" fill="none" stroke="#999" stroke-width="1.5"/></svg></span></div>
  <div class="list-row" style="top:863px;padding-left:17px">Completed Jobs<span class="row-action"><span class="count">5</span>View Details<svg width="8" height="12" viewBox="0 0 8 12"><path d="M1.5 1l5 5-5 5" fill="none" stroke="#999" stroke-width="1.5"/></svg></span></div>
</section>

</body>
</html>
```